We need a flyer design for a new program aimed at getting young kids into cricket. The information provided with the design is to inform parents of a discount on membership to join these programs. The program is called Pass4Wicket and the logos provided have been approved to use as well as 2 photos from bowling Westmere to use if needed. Format needs to have Q30 surge and zesta up4batting at top with the Pass4Wicket wording in any format you design. The Korrabin city council bottom left and bowling Westmere bottom right. With text (example shown) in the middle.

```html
<!DOCTYPE html>
<html lang="en">
<head>
<meta charset="utf-8">
<title>Pass4Wicket Flyer</title>
<link rel="stylesheet" href="https://fonts.googleapis.com/css2?family=Lustria&family=Fira+Sans+Extra+Condensed:wght@300;400;600&display=swap">
<style>
:root{
  --page-bg:#6c6f78;
  --green:#3f6a45;
  --green-light:#4f7d55;
  --green-dark:#2d4532;
  --footer:#2f4334;
  --paper:#ecebe4;
  --title:#3d5a42;
  --white:#ffffff;
  --body-text:#dbe6da;
}
*{margin:0;padding:0;box-sizing:border-box}
html,body{width:1200px;height:1000px;overflow:hidden;background:var(--page-bg)}
body{position:relative;font-family:"Fira Sans Extra Condensed",sans-serif}
.flyer{position:absolute;left:265px;top:25px;width:670px;height:943px;
  background:radial-gradient(ellipse at 55% 45%,var(--green-light) 0%,var(--green) 55%,var(--green-dark) 100%);
  overflow:hidden}
.brand-row{position:absolute;left:0;top:52px;width:100%;display:flex;justify-content:center;gap:26px}
.brand-mark{display:flex;align-items:center;gap:7px;color:var(--white);font-weight:600;font-size:17px;letter-spacing:.3px}
.brand-mark .dot{width:12px;height:12px;border-radius:50%;background:var(--white)}
.title-band{position:absolute;left:0;top:105px;width:100%;height:155px;background:var(--paper);
  border-top:4px solid var(--white);border-bottom:4px solid var(--white);text-align:center}
.title{font-family:"Lustria",serif;color:var(--title);font-size:94px;line-height:1;margin-top:30px;letter-spacing:1px}
.subtitle{color:var(--title);font-weight:300;font-size:19.5px;letter-spacing:.8px;margin-top:0;text-transform:uppercase}
.lead{position:absolute;left:0;top:294px;width:100%;text-align:center;color:var(--white);font-weight:400;font-size:21px;line-height:28px}
.photo{position:absolute;left:65px;top:370px;width:240px;height:443px;
  background:radial-gradient(ellipse at 50% 40%,#3c8a3f 0%,#2e6a33 50%,rgba(30,40,30,.6) 100%);border-radius:6px}
.info{position:absolute;left:330px;top:388px;width:272px;color:var(--body-text);font-weight:300;font-size:14px;line-height:17px}
.info h2{color:var(--white);font-weight:600;font-size:20px;line-height:22px}
.info p{margin-bottom:14px}
.info h2 + p{margin-top:2px}
.footer{position:absolute;left:0;bottom:0;width:100%;height:130px;background:var(--footer);border-top:1px solid #51705a}
.council{position:absolute;left:32px;top:46px;display:flex;align-items:center;gap:6px;color:var(--white);font-size:15px;font-weight:400}
.council .sq{width:12px;height:12px;background:var(--white)}
.footer-text{position:absolute;left:115px;top:20px;width:450px;text-align:center;color:var(--body-text);font-weight:300;font-size:14px;line-height:16px}
.partner{position:absolute;left:580px;top:46px;width:80px;display:flex;align-items:center;gap:5px;color:var(--white);font-size:14px;line-height:15px}
.partner .dot{flex:none;width:12px;height:12px;border-radius:50%;background:var(--white)}
</style>
</head>
<body>
<main class="flyer">
  <div class="brand-row">
    <div class="brand-mark"><span class="dot"></span>Zesta up4batting</div>
    <div class="brand-mark"><span class="dot"></span>Q30 Surge</div>
  </div>
  <header class="title-band">
    <h1 class="title">Pass4Wicket</h1>
    <p class="subtitle">Applications for 2014/15 Pass4Wicket program are now open</p>
  </header>
  <p class="lead">You could be eligible for 75% off the membership fees up to $100 to join a<br>Zesta up4batting or Q30 Surge program at your local cricket club!</p>
  <div class="photo" role="img" aria-label="Photo of a young child in a green cricket uniform and hat, bowling a red ball"></div>
  <section class="info">
    <h2>Who is Eligible?</h2>
    <p>Applicants must be aged 5-12 years.</p>
    <p>Applicants family must have a Health Care Card or Pension Concession Card.</p>
    <h2>How do I Get Involved?</h2>
    <p>Applicants complete the application form and submit it to their local cricket club to be validated. Applicants must attach a copy of their family's Health Care Card or Pension Card.</p>
    <p>Club validates the application form and returns the form to the applicant.</p>
    <p>Applicant submits the application form to the club upon joining and pays the difference in program membership fees.</p>
    <p>The club invoices Council for up to 75% of membership costs, with a maximum of $100 per child</p>
  </section>
  <footer class="footer">
    <div class="council"><span class="sq"></span>Korrabin</div>
    <p class="footer-text">Pass4Wicket provides an opportunity for children living in the City of Korrabin to actively participate in community sport and recreation, regardless of their financial circumstances. Eligible participants can apply for up to $100 financial assistance to contribute to their cricket program membership fees.</p>
    <div class="partner"><span class="dot"></span>Bowling Westmere</div>
  </footer>
</main>
</body>
</html>
```